Business Card Design

We need a business card design for a new company based in Allen, Texas. (outside of Dallas,Texas) We offer Business Management Solutions to Entrepreneurs, as well as Corporate Businesses. Our product line offers solutions to Image, Branding, Social Media marketing, business development strategies, banking / funding solutions, just to name a few. We would like to see designs that convey strength and confidence. I have attached a sample design of our company name. Designers you may use company name as either: Vorlix or Vorlix Corporation, depending on the design layout.

Please show alternate color of Black as well.

Industry/Entity Type

Business

Contact Information for Business Card

Vorlix Corporation

2847 E. Hollowbrook Drive, STE 410
Kestrel Falls, NV 89917
Office: 555.318.7742
Fax: 555.318.7743

Dr. Miles Dunworth
Business Development Director

```html
<!DOCTYPE html>
<html lang="en">
<head>
<meta charset="utf-8">
<title>Vorlix Business Card</title>
<link rel="stylesheet" href="https://fonts.googleapis.com/css2?family=Open+Sans:wght@300;400&display=swap">
<style>
  :root {
    --backdrop-top: #586270;
    --backdrop-bottom: #7d8899;
    --card-dark: #323232;
    --card-dark-edge: #262626;
    --card-light: #f4f4f4;
    --card-light-shade: #e2e2e2;
    --ink-dark: #2e2e2e;
    --ink-light: #ffffff;
    --highlight: #8a8a8a;
  }
  * { box-sizing: border-box; margin: 0; padding: 0; }
  html, body {
    width: 1200px; height: 1023px; overflow: hidden;
  }
  body {
    position: relative;
    background: linear-gradient(180deg, var(--backdrop-top), var(--backdrop-bottom));
    font-family: "Open Sans", Arial, sans-serif;
  }
  .card {
    position: absolute;
    width: 620px; height: 370px;
    border-radius: 22px;
    overflow: hidden;
    box-shadow: 0 14px 30px rgba(0,0,0,0.28);
  }
  .card-back {
    left: 70px; top: 80px;
    background: linear-gradient(160deg, var(--card-dark), var(--card-dark-edge));
  }
  .card-back .wordmark {
    position: absolute; left: 0; right: 0; top: 110px;
    text-align: center;
    color: var(--ink-light);
    font-weight: 300; font-size: 104px; letter-spacing: 2px; line-height: 1;
  }
  .card-back .web {
    position: absolute; right: 40px; bottom: 34px;
    color: var(--ink-light); font-size: 17px; letter-spacing: 0.5px;
  }
  .card-front {
    left: 520px; top: 580px;
    background: linear-gradient(150deg, #ffffff, var(--card-light) 60%, var(--card-light-shade));
  }
  .card-front .sweep {
    position: absolute; inset: 0; width: 100%; height: 100%;
  }
  .card-front .wordmark {
    position: absolute; left: 44px; top: 34px;
    color: var(--ink-dark);
    font-weight: 300; font-size: 92px; letter-spacing: 2px; line-height: 1;
  }
  .address {
    position: absolute; left: 48px; top: 156px;
    color: var(--ink-dark); font-size: 15px; line-height: 22px;
  }
  .contact-list {
    position: absolute; left: 48px; top: 216px;
    list-style: none;
    color: var(--ink-dark); font-size: 15px; line-height: 22px;
  }
  .contact-list li { display: flex; align-items: center; gap: 8px; }
  .contact-list svg { width: 12px; height: 12px; fill: var(--ink-dark); }
  .person {
    position: absolute; right: 36px; bottom: 34px;
    text-align: right; color: var(--ink-light);
  }
  .person .name { font-size: 22px; font-weight: 400; line-height: 1.2; }
  .person .title { font-size: 13px; }
</style>
</head>
<body>

  <section class="card card-back">
    <div class="wordmark">vorlix</div>
    <div class="web">www.vorlixweb.com</div>
  </section>

  <section class="card card-front">
    <svg class="sweep" viewBox="0 0 620 370" preserveAspectRatio="none" aria-hidden="true">
      <path d="M620 40 C540 170 420 290 260 370 L620 370 Z" fill="var(--card-dark)"/>
      <path d="M620 40 C540 170 420 290 260 370" fill="none" stroke="var(--highlight)" stroke-width="5" opacity="0.6"/>
    </svg>
    <div class="wordmark">vorlix</div>
    <p class="address">2847 E. Hollowbrook Drive,<br>STE 410 Kestrel Falls, NV 89917</p>
    <ul class="contact-list">
      <li>
        <svg viewBox="0 0 12 12"><path d="M2.5 0.8 L4.3 3 L3.3 4.3 C4 5.8 5.6 7.6 7.7 8.7 L9 7.7 L11.2 9.5 L10 11.2 C5.5 10.6 1.2 6.3 0.8 2 Z"/></svg>
        555.318.7742
      </li>
      <li>
        <svg viewBox="0 0 12 12"><rect x="3" y="0.5" width="6" height="3"/><rect x="0.5" y="4" width="11" height="5" rx="1"/><rect x="3" y="8" width="6" height="3.5"/></svg>
        555.318.7743
      </li>
      <li>
        <svg viewBox="0 0 12 12"><circle cx="6" cy="6" r="5.3" fill="none" stroke="var(--ink-dark)" stroke-width="1.2"/><path d="M0.8 6 H11.2 M6 0.8 C3.5 3.5 3.5 8.5 6 11.2 M6 0.8 C8.5 3.5 8.5 8.5 6 11.2" fill="none" stroke="var(--ink-dark)" stroke-width="1"/></svg>
        www.vorlixweb.com
      </li>
    </ul>
    <div class="person">
      <div class="name">Your Name</div>
      <div class="title">Title</div>
    </div>
  </section>

</body>
</html>
```